Business Card Design for C oastal M eadowherb T hriving I nitiative

business card for non-profit
-use logo uploaded (thanks artist plumtoad)
-include c m t i. o r g website and include the three names - titles - emails from website
-recognize sponsors on the card somehow. logos or names?
Halvern Greenhouse Circle Association, Mossridge Plot Society of Olm and Tessel Greenway Foundation

-include colony of1) Trillium ovatum on the card or maybe Erythronium revolutum
or 2) just keep it simple with the logo

-single sided card is fine but I am posting double sided as an option as I am guessing that all this writing may require two sides.

Target Market(s)
-people who have plants and or time to contribute

Business Card Design Requirements
Must Have:
- Project Name
- Contact info
- Website

Industry/Entity Type

Business

Requirements
Must have
• All four contacts on the card please,
• Meadowherb Thriving Initiative Coordinator - Dorian - coastalmeadowherb@ kelvimail.com
• Nursery Operations Coordinator - Milo - nursery.cmti@ kelvimail.com
• Seed Collection Coordinator - Milo - seeds.cmti@kelvimail.com
• Plant Rescue Operations Coordinator- Edith - plantrescue.cmti@ kelvimail.com

```html
<!DOCTYPE html>
<html lang="en">
<head>
<meta charset="utf-8">
<title>Coastal Meadowherb Thriving Initiative – Business Card</title>
<link rel="stylesheet" href="https://fonts.googleapis.com/css2?family=Roboto+Condensed:wght@400;700&display=swap">
<style>
  :root {
    --page-bg: #e4e4e6;
    --card-white-edge: #e6e6e6;
    --band-dark: #333333;
    --leaf-green: #65b950;
    --foliage-dark: #2f4d2c;
    --foliage-mid: #4f7d47;
    --ink: #1e1e1e;
    --ink-soft: #2e3a2b;
    --white: #ffffff;
    --brace: #7a8a72;
  }
  html, body {
    margin: 0;
    width: 1200px;
    height: 1200px;
    overflow: hidden;
    background: var(--page-bg);
  }
  .canvas {
    position: relative;
    width: 1200px;
    height: 1200px;
  }
  .card {
    position: absolute;
    left: 153px;
    width: 839px;
    height: 475px;
    display: block;
  }
  .card--front { top: 74px; }
  .card--back  { top: 634px; }
  .card text { font-family: "Roboto Condensed", sans-serif; }
  .brand-name { fill: var(--ink); font-weight: 400; }
  .tagline { fill: var(--white); font-size: 31px; }
  .sponsors { fill: var(--white); font-size: 18px; }
  .coordinator-name { fill: var(--white); font-weight: 700; font-size: 20px; }
  .coordinator-role { fill: var(--ink-soft); font-weight: 400; font-size: 20px; }
  .coordinator-email { fill: var(--ink); font-size: 19px; }
  .contact-line { fill: var(--ink); font-size: 30px; }
  .contact-icon { fill: none; stroke: var(--white); stroke-width: 2.2; }
</style>
</head>
<body>
<main class="canvas">

  <!-- Front of card -->
  <svg class="card card--front" viewBox="0 0 1049 594" xmlns="http://www.w3.org/2000/svg">
    <defs>
      <radialGradient id="front-paper" cx="0.5" cy="0.3" r="0.7">
        <stop offset="0" stop-color="#fbfbfb"/>
        <stop offset="1" stop-color="var(--card-white-edge)"/>
      </radialGradient>
      <linearGradient id="front-foliage" x1="0" y1="0" x2="1" y2="1">
        <stop offset="0" stop-color="var(--foliage-mid)"/>
        <stop offset="0.5" stop-color="var(--foliage-dark)"/>
        <stop offset="1" stop-color="var(--foliage-mid)"/>
      </linearGradient>
      <filter id="tagline-shadow" x="-5%" y="-30%" width="110%" height="160%">
        <feDropShadow dx="1" dy="2" stdDeviation="2" flood-color="#000" flood-opacity="0.85"/>
      </filter>
    </defs>

    <rect class="foliage-photo" role="img" aria-label="Photograph of a colony of Trillium ovatum flowers among green leaves"
          x="0" y="290" width="1049" height="304" fill="url(#front-foliage)"/>
    <path class="accent-band" d="M0 305 Q480 400 1049 262 L1049 312 Q520 410 0 312 Z" fill="var(--band-dark)"/>
    <path class="paper-top" d="M0 0 H1049 V262 Q480 400 0 305 Z" fill="url(#front-paper)"/>

    <circle class="brand-dot" cx="534" cy="128" r="26" fill="var(--leaf-green)"/>
    <text class="brand-name" x="534" y="222" text-anchor="middle" font-size="50">Coastal Meadowherb</text>
    <text class="brand-name" x="534" y="274" text-anchor="middle" font-size="50">Thriving Initiative</text>

    <g class="tagline" filter="url(#tagline-shadow)">
      <text x="508" y="470" text-anchor="middle">A plan for sustaining and enhancing the native wildflower presence</text>
      <text x="508" y="508" text-anchor="middle">in the regional and city parks of Metro Halvern.</text>
    </g>

    <text class="sponsors" x="524" y="568" text-anchor="middle" filter="url(#tagline-shadow)">Supported by Halvern Greenhouse Circle Association · Mossridge Plot Society of Olm · Tessel Greenway Foundation</text>
  </svg>

  <!-- Back of card -->
  <svg class="card card--back" viewBox="0 0 1049 594" xmlns="http://www.w3.org/2000/svg">
    <defs>
      <radialGradient id="back-paper" cx="0.25" cy="0.3" r="0.7">
        <stop offset="0" stop-color="#fbfbfb"/>
        <stop offset="1" stop-color="var(--card-white-edge)"/>
      </radialGradient>
      <linearGradient id="back-foliage" x1="0" y1="0" x2="1" y2="0">
        <stop offset="0" stop-color="#f4f4f4" stop-opacity="0"/>
        <stop offset="0.25" stop-color="#a9bca4" stop-opacity="0.7"/>
        <stop offset="0.55" stop-color="var(--foliage-mid)"/>
        <stop offset="1" stop-color="var(--foliage-dark)"/>
      </linearGradient>
    </defs>

    <rect class="paper" x="0" y="0" width="1049" height="594" fill="url(#back-paper)"/>
    <path class="foliage-photo" role="img" aria-label="Close-up photograph of pale pink trillium flowers with broad green leaves"
          d="M420 0 H1049 V300 Q700 360 420 340 Z" fill="url(#back-foliage)"/>
    <path class="accent-band" d="M300 322 Q700 350 1049 255 L1049 300 Q700 365 300 330 Z" fill="var(--band-dark)"/>
    <path class="green-panel" d="M0 270 Q300 345 600 338 Q850 330 1049 295 V594 H0 Z" fill="var(--leaf-green)"/>

    <circle class="brand-dot" cx="244" cy="110" r="22" fill="var(--leaf-green)"/>
    <text class="brand-name" x="244" y="185" text-anchor="middle" font-size="40">Coastal Meadowherb</text>
    <text class="brand-name" x="244" y="229" text-anchor="middle" font-size="40">Thriving Initiative</text>

    <g class="coordinators">
      <text x="40" y="378"><tspan class="coordinator-name">Dorian</tspan><tspan class="coordinator-role" dx="8">Meadowherb Thriving Initiative Coordinator</tspan></text>
      <text class="coordinator-email" x="40" y="401">coastalmeadowherb@kelvimail.com</text>

      <text x="40" y="433"><tspan class="coordinator-name">Milo</tspan><tspan class="coordinator-role" dx="8">Nursery Operations Coordinator</tspan></text>
      <text class="coordinator-email" x="40" y="456">nursery.cmti@kelvimail.com</text>

      <text x="40" y="488"><tspan class="coordinator-name">Milo</tspan><tspan class="coordinator-role" dx="8">Seed Collection Coordinator</tspan></text>
      <text class="coordinator-email" x="40" y="511">seeds.cmti@kelvimail.com</text>

      <text x="40" y="543"><tspan class="coordinator-name">Edith</tspan><tspan class="coordinator-role" dx="8">Plant Rescue Operations Coordinator</tspan></text>
      <text class="coordinator-email" x="40" y="566">plantrescue.cmti@kelvimail.com</text>
    </g>

    <path class="brace" d="M484 382 Q470 386 472 412 L472 442 Q472 452 466 454 Q472 456 472 466 L472 496 Q470 520 484 524"
          fill="none" stroke="var(--brace)" stroke-width="2"/>

    <g class="contact">
      <path class="contact-icon" d="M515 404 q-6 4 -2 16 q5 13 14 17 q6 2 9 -3 l-6 -6 q-3 3 -6 0 q-4 -5 -5 -10 q-1 -3 2 -4 z"
            fill="var(--white)"/>
      <text class="contact-line" x="557" y="430">555.014.0188</text>

      <g class="contact-icon">
        <circle cx="526" cy="484" r="12"/>
        <ellipse cx="526" cy="484" rx="5" ry="12"/>
        <line x1="514" y1="484" x2="538" y2="484"/>
        <line x1="516" y1="478" x2="536" y2="478"/>
        <line x1="516" y1="490" x2="536" y2="490"/>
      </g>
      <text class="contact-line" x="557" y="494" letter-spacing="3">c m t i. o r g</text>
    </g>
  </svg>

</main>
</body>
</html>
```